New Menu Design Project

Would like a menu designed..

SIZE A4 - double sided..

One on side, we would like our regular menu, on the other side we would like our catering options.
I have attached both files/
I have also attached our logo

Target Market(s)

We are located at a hospital, so we target hospital staff and also university students.

Industry/Entity Type

Catering

```html
<!DOCTYPE html>
<html lang="en">
<head>
<meta charset="utf-8">
<title>Ward Nine Canteen – Menu</title>
<link href="https://fonts.googleapis.com/css2?family=Montserrat:wght@400;500;600&display=swap" rel="stylesheet">
<style>
  :root {
    --brand-red: #e3003a;
    --panel-grey: #e6e6e6;
    --ink: #111111;
    --white: #ffffff;
  }
  html, body {
    margin: 0;
    padding: 0;
    overflow: hidden;
  }
  body {
    width: 848px;
    height: 1200px;
    font-family: "Montserrat", Arial, sans-serif;
    color: var(--ink);
  }
  .menu-sheet {
    position: relative;
    width: 848px;
    height: 1200px;
    background: var(--brand-red);
    overflow: hidden;
  }
  .title-bar {
    position: absolute;
    left: 225px;
    top: 51px;
    width: 549px;
    height: 92px;
    background: var(--white);
  }
  .title-bar h1 {
    position: absolute;
    left: 36px;
    top: 50%;
    transform: translateY(-50%);
    margin: 0;
    font-size: 58px;
    font-weight: 500;
    letter-spacing: 1px;
    line-height: 1;
  }
  .brand-mark {
    position: absolute;
    left: 28px;
    top: 22px;
    width: 176px;
    height: 176px;
    border-radius: 50%;
    background: var(--white);
    display: flex;
    align-items: center;
    justify-content: center;
  }
  .brand-mark span {
    font-size: 27px;
    font-weight: 600;
    color: var(--brand-red);
    text-align: center;
    line-height: 1.1;
  }
  .preorder {
    position: absolute;
    left: 237px;
    top: 160px;
    margin: 0;
    color: var(--white);
    font-size: 20px;
    font-weight: 500;
    white-space: nowrap;
  }
  .preorder strong {
    font-size: 29px;
    font-weight: 500;
    letter-spacing: 0.5px;
  }
  .menu-panel {
    position: absolute;
    left: 33px;
    top: 217px;
    width: 784px;
    height: 944px;
    background: var(--panel-grey);
  }
  .menu-section {
    position: absolute;
  }
  .menu-section h2 {
    margin: 0 0 15px;
    font-size: 30px;
    font-weight: 500;
    letter-spacing: 0.5px;
    line-height: 1;
  }
  .item-list {
    list-style: none;
    margin: 0;
    padding: 0 0 0 5px;
  }
  .item-list li {
    display: flex;
    height: 27px;
    align-items: center;
    font-size: 16px;
    font-weight: 400;
    white-space: nowrap;
  }
  .item-list .price {
    color: var(--brand-red);
    font-weight: 600;
  }
  .section-light { left: 41px; top: 30px; }
  .section-breakfast { left: 412px; top: 30px; }
  .section-hot { left: 41px; top: 372px; }
  .section-burgers { left: 41px; top: 731px; }
  .section-light .item-name,
  .section-hot .item-name { width: 256px; }
  .section-breakfast .item-name { width: 256px; }
  .section-burgers .item-name { width: 437px; }
</style>
</head>
<body>
<main class="menu-sheet">
  <div class="brand-mark"><span>Ward<br>Nine</span></div>
  <header class="title-bar"><h1>MENU</h1></header>
  <p class="preorder">Phone or text <strong>0491 570 156</strong> to pre order</p>

  <section class="menu-panel">
    <div class="menu-section section-light">
      <h2>SOMETHING LIGHT</h2>
      <ul class="item-list">
        <li><span class="item-name">Mixed yoghurts</span><span class="price">$6</span></li>
        <li><span class="item-name">Chia puddings</span><span class="price">$5.50</span></li>
        <li><span class="item-name">Fruit salad</span><span class="price">$5</span></li>
        <li><span class="item-name">Bircher muesli</span><span class="price">$6.00</span></li>
        <li><span class="item-name">Homemade muffins</span><span class="price">$5.50</span></li>
        <li><span class="item-name">Banana bread</span><span class="price">$3.50</span></li>
        <li><span class="item-name">Cookies</span><span class="price">$4</span></li>
        <li><span class="item-name">Slices</span><span class="price">$1.50</span></li>
      </ul>
    </div>

    <div class="menu-section section-breakfast">
      <h2>BREAKFAST ITEMS</h2>
      <ul class="item-list">
        <li><span class="item-name">Egg, bacon &amp; cheese roll</span><span class="price">$6</span></li>
        <li><span class="item-name">Ham &amp; cheese toastie</span><span class="price">$5.50</span></li>
        <li><span class="item-name">Cheese &amp; tomato toastie</span><span class="price">$5</span></li>
        <li><span class="item-name">Ham &amp; cheese croissant</span><span class="price">$6.00</span></li>
        <li><span class="item-name">Cheese &amp; tomato croissant</span><span class="price">$5.50</span></li>
        <li><span class="item-name">Plain croissant</span><span class="price">$3.50</span></li>
        <li><span class="item-name">Toasted w/spreads</span><span class="price">$4</span></li>
        <li><span class="item-name">Hash brown</span><span class="price">$1.50</span></li>
        <li><span class="item-name">2 piece toast w/spreads</span><span class="price">$3</span></li>
        <li><span class="item-name">2 piece rasin toast</span><span class="price">$3</span></li>
      </ul>
    </div>

    <div class="menu-section section-hot">
      <h2>HOT FOOD &amp; SANDWICHES</h2>
      <ul class="item-list">
        <li><span class="item-name">Egg, bacon &amp; cheese roll</span><span class="price">$6</span></li>
        <li><span class="item-name">Ham &amp; cheese toastie</span><span class="price">$5.50</span></li>
        <li><span class="item-name">Cheese &amp; tomato toastie</span><span class="price">$5</span></li>
        <li><span class="item-name">Ham &amp; cheese croissant</span><span class="price">$6.00</span></li>
        <li><span class="item-name">Cheese &amp; tomato croissant</span><span class="price">$5.50</span></li>
        <li><span class="item-name">Plain croissant</span><span class="price">$3.50</span></li>
        <li><span class="item-name">Toasted w/spreads</span><span class="price">$4</span></li>
        <li><span class="item-name">Hash brown</span><span class="price">$1.50</span></li>
        <li><span class="item-name">2 piece toast w/spreads</span><span class="price">$3</span></li>
        <li><span class="item-name">2 piece rasin toast</span><span class="price">$3</span></li>
      </ul>
    </div>

    <div class="menu-section section-burgers">
      <h2>BURGERS</h2>
      <ul class="item-list">
        <li><span class="item-name">Plain hamburger - tomato, onion, lettuce, sauce</span><span class="price">$6</span></li>
        <li><span class="item-name">Hamburger with the lot - plain plus beetroot</span><span class="price">$5.50</span></li>
        <li><span class="item-name">Schnitzel burger - homemade breast fillet</span><span class="price">$5</span></li>
        <li><span class="item-name">Extras - beetroot, egg, cheese, bacon, 50c</span><span class="price">$6.00</span></li>
      </ul>
    </div>
  </section>
</main>
</body>
</html>
```